Dental Business Card

We are looking for a double sided business card that can be easily customized with the names of the different members of our dental team.

I would like the background to be the 2-tone blue fleur-de-lis type pattern on the sides of our website (www.harborlanegrins.com).

I would like the logo attached incorporated.

I would like our address (4872 Pell Orchard Drive, Suite 100, Marlow Creek, MD 23412), phone number (757-318-4590), fax number (757-318-2764), website (www.harborlanegrins.com), and email address (info@harborlanegrins.com) all included on the front side.

Something a little more artistic to complement/highlight the logo on the back would be interesting.

I would like the business card to look professional, slightly feminine, and expense.

Reason: Still looking for the perfect design.

```html
<!DOCTYPE html>
<html lang="en">
<head>
<meta charset="utf-8">
<title>Harbor Lane Grins – Business Card</title>
<link rel="stylesheet" href="https://fonts.googleapis.com/css2?family=Cinzel:wght@400;600&family=Open+Sans:wght@400;600&display=swap">
<style>
  :root {
    --backdrop: #ecedef;
    --navy-blue: #1c6cb5;
    --royal-blue: #2f86cc;
    --sky-blue: #5aaedc;
    --mist-blue: #d3e6f3;
    --pale-blue: #e6f1f9;
    --logo-blue: #3b7fc1;
    --ink-blue: #2b67a2;
    --white: #ffffff;
  }
  html, body {
    margin: 0;
    width: 1200px;
    height: 800px;
    overflow: hidden;
    background: var(--backdrop);
  }
  .canvas {
    position: relative;
    width: 1200px;
    height: 800px;
  }
  .card {
    position: absolute;
    overflow: hidden;
    border-radius: 4px;
    box-shadow: 0 10px 28px rgba(30, 60, 100, 0.22);
  }
  .card svg.card-art {
    position: absolute;
    inset: 0;
  }

  /* Back side (vertical) */
  .card-back {
    left: 90px;
    top: 110px;
    width: 330px;
    height: 580px;
  }
  .back-brand {
    position: absolute;
    right: 22px;
    top: 30px;
    writing-mode: vertical-rl;
    display: flex;
    flex-direction: column;
    gap: 6px;
    align-items: center;
    color: var(--white);
    font-family: "Cinzel", serif;
  }
  .back-brand .brand-name {
    font-size: 22px;
    letter-spacing: 1px;
  }
  .back-brand .tagline {
    font-size: 10px;
    letter-spacing: 1px;
    display: flex;
    align-items: center;
    gap: 8px;
  }
  .back-brand .tagline::before,
  .back-brand .tagline::after {
    content: "";
    width: 1px;
    height: 22px;
    background: var(--white);
  }

  /* Front side (horizontal) */
  .card-front {
    left: 470px;
    top: 215px;
    width: 640px;
    height: 370px;
  }
  .front-brand {
    position: absolute;
    left: 262px;
    top: 26px;
    width: 360px;
    text-align: center;
    font-family: "Cinzel", serif;
    color: var(--logo-blue);
  }
  .front-brand .brand-line {
    display: flex;
    align-items: center;
    justify-content: center;
    gap: 10px;
  }
  .front-brand .brand-mark {
    width: 16px;
    height: 16px;
    border-radius: 50%;
    background: var(--logo-blue);
  }
  .front-brand .brand-name {
    font-size: 30px;
    font-weight: 400;
    letter-spacing: 1px;
  }
  .front-brand .tagline {
    margin-top: 4px;
    font-size: 15px;
    letter-spacing: 1px;
    display: flex;
    align-items: center;
    justify-content: center;
    gap: 10px;
  }
  .front-brand .tagline::before,
  .front-brand .tagline::after {
    content: "";
    width: 46px;
    height: 1px;
    background: var(--logo-blue);
  }
  .member {
    position: absolute;
    left: 30px;
    top: 196px;
    color: var(--white);
  }
  .member .member-name {
    font-family: "Cinzel", serif;
    font-size: 25px;
    letter-spacing: 1px;
  }
  .member .member-role {
    font-family: "Open Sans", sans-serif;
    font-size: 12px;
    margin-top: 2px;
  }
  .contact-list {
    position: absolute;
    left: 300px;
    top: 246px;
    margin: 0;
    padding: 0;
    list-style: none;
    font-family: "Open Sans", sans-serif;
    font-size: 14px;
    color: var(--white);
    line-height: 21px;
  }
  .contact-list li {
    display: flex;
    align-items: center;
    gap: 9px;
  }
  .contact-list .icon {
    width: 14px;
    height: 14px;
    flex: none;
  }
  .contact-list .web {
    padding-left: 23px;
  }
  .address {
    font-family: "Open Sans", sans-serif;
    font-size: 13px;
    fill: var(--ink-blue);
  }
</style>
</head>
<body>
<main class="canvas">

  <section class="card card-back" aria-label="Business card, back">
    <svg class="card-art" width="330" height="580" viewBox="0 0 330 580">
      <defs>
        <linearGradient id="back-top" x1="0" y1="0" x2="1" y2="1">
          <stop offset="0" stop-color="#2a80c8"/>
          <stop offset="1" stop-color="#1a67b1"/>
        </linearGradient>
        <radialGradient id="back-deco" cx="0.45" cy="0.6" r="0.6">
          <stop offset="0" stop-color="#9cc8e8"/>
          <stop offset="1" stop-color="#d3e6f3"/>
        </radialGradient>
      </defs>
      <rect width="330" height="580" fill="url(#back-top)"/>
      <path d="M0 350 C 110 330 230 310 330 260 L330 580 L0 580 Z" fill="var(--mist-blue)"/>
      <path d="M0 360 C 120 338 240 320 330 273 L330 580 L0 580 Z"
            fill="url(#back-deco)" role="img"
            aria-label="Two-tone blue damask pattern with a large faint decoration"/>
      <path d="M40 342 C 140 332 250 300 330 247" fill="none" stroke="var(--sky-blue)" stroke-width="6"/>
    </svg>
    <div class="back-brand">
      <span class="brand-name">Harbor Lane Grins</span>
      <span class="tagline">The Craft of Smiles</span>
    </div>
  </section>

  <section class="card card-front" aria-label="Business card, front">
    <svg class="card-art" width="640" height="370" viewBox="0 0 640 370">
      <defs>
        <linearGradient id="front-blue" x1="0" y1="0" x2="0.3" y2="1">
          <stop offset="0" stop-color="#62b3df"/>
          <stop offset="0.55" stop-color="#3d93d0"/>
          <stop offset="1" stop-color="#1c6cb5"/>
        </linearGradient>
      </defs>
      <rect width="640" height="370" fill="var(--mist-blue)" role="img"
            aria-label="Two-tone blue damask pattern background"/>
      <path d="M0 118 C 230 70 450 190 640 285 L640 370 L0 370 Z" fill="var(--white)"/>
      <path d="M60 108 C 260 80 450 180 640 268" fill="none" stroke="var(--pale-blue)" stroke-width="5"/>
      <path d="M0 162 C 230 122 440 237 640 332 L640 370 L0 370 Z" fill="url(#front-blue)"/>
      <path id="address-path" d="M14 143 C 235 100 445 214 640 308" fill="none"/>
      <text class="address">
        <textPath href="#address-path" startOffset="6">4872 Pell Orchard Drive, Suite 100, Marlow Creek, MD 23412</textPath>
      </text>
    </svg>

    <div class="front-brand">
      <div class="brand-line">
        <span class="brand-mark"></span>
        <span class="brand-name">Harbor Lane Grins</span>
      </div>
      <div class="tagline">The Craft of Smiles</div>
    </div>

    <div class="member">
      <div class="member-name">Nora Pellam</div>
      <div class="member-role">Director</div>
    </div>

    <ul class="contact-list">
      <li>
        <svg class="icon" viewBox="0 0 14 14" aria-hidden="true"><circle cx="7" cy="7" r="7" fill="#ffffff"/><path d="M4.4 3.6l1.4-.3.7 1.7-.9.7c.5 1 1.2 1.7 2.2 2.2l.7-.9 1.7.7-.3 1.4C7.2 9.8 4.2 6.8 4.4 3.6z" fill="#1c6cb5"/></svg>
        757-318-4590
      </li>
      <li>
        <svg class="icon" viewBox="0 0 14 14" aria-hidden="true"><circle cx="7" cy="7" r="7" fill="#ffffff"/><rect x="4" y="5.5" width="6" height="4" fill="#1c6cb5"/><rect x="5" y="3.5" width="4" height="2" fill="#1c6cb5"/></svg>
        757-318-2764
      </li>
      <li>
        <svg class="icon" viewBox="0 0 14 14" aria-hidden="true"><circle cx="7" cy="7" r="7" fill="#ffffff"/><rect x="3.5" y="4.5" width="7" height="5" fill="none" stroke="#1c6cb5"/><path d="M3.5 4.5L7 7.5l3.5-3" fill="none" stroke="#1c6cb5"/></svg>
        info@harborlanegrins.com
      </li>
      <li class="web">www.harborlanegrins.com</li>
    </ul>
  </section>

</main>
</body>
</html>
```